Financial Advisor needs a NEW business card design

We need a new card design as our current design has no white space and clients tend to want to write on the card. I am attaching our current logos and current card design. I have also played with some designs I liked online but don't have the knowledge (or software) to complete the designs in a format that is appropriate for production. I've attached those designs that I liked too. With two office locations and a disclaimer there is a lot of info but we want it to look tidy. We like the deep, rich blue colors and want it to look clean, strong, and modern yet classic.
Business
Included in the attached files

```html
<!DOCTYPE html>
<html lang="en">
<head>
<meta charset="utf-8">
<title>Kestrel Wealth Advisory – Business Card</title>
<link href="https://fonts.googleapis.com/css2?family=PT+Serif:ital,wght@0,400;0,700;1,400&display=swap" rel="stylesheet">
<style>
  :root {
    --backdrop: #e4e4e6;
    --navy: #1f2f5c;
    --navy-deep: #192650;
    --white-card: #f6f6f6;
    --ink: #2a2a2e;
    --rule: #7d7d80;
    --on-navy: #f2f2f4;
    --accent-ink: #2c3c6c;
  }
  * { margin: 0; padding: 0; box-sizing: border-box; }
  html, body { width: 1200px; height: 852px; overflow: hidden; }
  body {
    background: var(--backdrop);
    font-family: "PT Serif", Georgia, serif;
    position: relative;
  }
  .card {
    position: absolute;
    top: 266px;
    width: 540px;
    height: 320px;
    border-radius: 28px;
    box-shadow: 0 6px 18px rgba(0,0,0,0.18);
  }
  .card--front {
    left: 40px;
    background: linear-gradient(135deg, var(--navy) 0%, var(--navy-deep) 100%);
    color: var(--on-navy);
  }
  .card--back {
    left: 620px;
    background: var(--white-card);
    color: var(--ink);
  }

  /* Front: brand */
  .front-brand {
    position: absolute;
    left: 96px;
    top: 78px;
    width: 350px;
    text-align: center;
  }
  .brand-name {
    font-size: 30px;
    font-weight: 400;
    letter-spacing: 0.04em;
    text-transform: uppercase;
    line-height: 1.15;
  }
  .front-brand .brand-name { color: var(--on-navy); }
  .brand-rule {
    height: 4px;
    background: var(--rule);
    margin-top: 14px;
  }

  /* Front: offices */
  .offices {
    position: absolute;
    left: 36px;
    right: 36px;
    bottom: 40px;
    display: flex;
    justify-content: space-between;
  }
  .office {
    display: flex;
    align-items: flex-start;
    gap: 10px;
    font-size: 15px;
    line-height: 1.35;
  }
  .office svg { flex: none; margin-top: 3px; }

  /* Back: brand */
  .back-brand {
    position: absolute;
    right: 34px;
    top: 40px;
    width: 260px;
    text-align: right;
  }
  .back-brand .brand-name {
    font-size: 19px;
    font-weight: 700;
    color: var(--accent-ink);
    letter-spacing: 0.02em;
  }
  .back-brand .brand-rule { height: 2px; margin-top: 8px; }

  .divider {
    position: absolute;
    left: 220px;
    right: 34px;
    top: 148px;
    height: 2px;
    background: var(--rule);
  }

  .disclaimer {
    position: absolute;
    right: 34px;
    top: 168px;
    width: 210px;
    text-align: right;
    font-size: 13px;
    line-height: 1.4;
  }

  /* Back: person & contacts */
  .person {
    position: absolute;
    left: 36px;
    top: 150px;
  }
  .person-name {
    font-size: 19px;
    font-weight: 700;
    color: var(--accent-ink);
  }
  .person-title {
    font-size: 13px;
    font-style: italic;
    margin-top: 2px;
  }
  .contacts {
    list-style: none;
    position: absolute;
    left: 56px;
    top: 212px;
    font-size: 15px;
    line-height: 1.45;
  }
  .contacts li {
    display: flex;
    align-items: center;
    gap: 10px;
  }
  .contacts svg { flex: none; }
  .contacts .note { color: var(--accent-ink); }
</style>
</head>
<body>

<section class="card card--front" aria-label="Card front">
  <div class="front-brand">
    <p class="brand-name">Kestrel Wealth Advisory</p>
    <div class="brand-rule"></div>
  </div>
  <div class="offices">
    <div class="office">
      <svg width="12" height="16" viewBox="0 0 12 16"><path d="M6 0a6 6 0 0 0-6 6c0 4.5 6 10 6 10s6-5.5 6-10a6 6 0 0 0-6-6z" fill="#f2f2f4"/><circle cx="6" cy="6" r="2.2" fill="#1f2f5c"/></svg>
      <p>2840 Mill Creek Road, Suite 210<br>Brookhaven, Texas 76010</p>
    </div>
    <div class="office">
      <svg width="12" height="16" viewBox="0 0 12 16"><path d="M6 0a6 6 0 0 0-6 6c0 4.5 6 10 6 10s6-5.5 6-10a6 6 0 0 0-6-6z" fill="#f2f2f4"/><circle cx="6" cy="6" r="2.2" fill="#1f2f5c"/></svg>
      <p>450 Lakeview Parkway, Suite 300<br>Ridgefield, Texas 75020</p>
    </div>
  </div>
</section>

<section class="card card--back" aria-label="Card back">
  <div class="back-brand">
    <p class="brand-name">Kestrel Wealth Advisory</p>
    <div class="brand-rule"></div>
  </div>
  <div class="divider"></div>
  <p class="disclaimer">Investment advisory services offered through Northgate Private Capital, LLC, an SEC Registered Investment Advisor</p>

  <div class="person">
    <p class="person-name">Daniel Whitcombe</p>
    <p class="person-title">Financial Advisor</p>
  </div>
  <ul class="contacts">
    <li>
      <svg width="13" height="13" viewBox="0 0 24 24"><path d="M6.6 10.8a15 15 0 0 0 6.6 6.6l2.2-2.2a1 1 0 0 1 1-.25 11.4 11.4 0 0 0 3.6.57 1 1 0 0 1 1 1V20a1 1 0 0 1-1 1A17 17 0 0 1 3 4a1 1 0 0 1 1-1h3.5a1 1 0 0 1 1 1c0 1.25.2 2.45.57 3.57a1 1 0 0 1-.25 1z" fill="#2c3c6c"/></svg>
      <span>555.210.0400 <span class="note">{Brookhaven}</span></span>
    </li>
    <li>
      <svg width="13" height="13" viewBox="0 0 24 24"><path d="M6.6 10.8a15 15 0 0 0 6.6 6.6l2.2-2.2a1 1 0 0 1 1-.25 11.4 11.4 0 0 0 3.6.57 1 1 0 0 1 1 1V20a1 1 0 0 1-1 1A17 17 0 0 1 3 4a1 1 0 0 1 1-1h3.5a1 1 0 0 1 1 1c0 1.25.2 2.45.57 3.57a1 1 0 0 1-.25 1z" fill="#2c3c6c"/></svg>
      <span>555.384.1927 <span class="note">{Ridgefield}</span></span>
    </li>
    <li>
      <svg width="14" height="11" viewBox="0 0 14 11"><rect width="14" height="11" rx="1" fill="#2c3c6c"/><path d="M1 1.5l6 4.5 6-4.5" stroke="#f6f6f6" stroke-width="1.2" fill="none"/></svg>
      <span>daniel@kestrelwealth.com</span>
    </li>
    <li>
      <svg width="13" height="13" viewBox="0 0 14 14"><circle cx="7" cy="7" r="6.5" fill="#2c3c6c"/><path d="M0.5 7h13M7 0.5c-3 3.5-3 9.5 0 13M7 0.5c3 3.5 3 9.5 0 13" stroke="#f6f6f6" stroke-width="0.9" fill="none"/></svg>
      <span>www.kestrelwealth.com</span>
    </li>
  </ul>
</section>

</body>
</html>
```